Mandala Postcard Design

I am in need of a postcard to hand out at a Psychic Fair. I envision the card to having half-of-a Mandala (from my Facebook folder), touched up a bit to make it vibrant and bold. Others vendors will have cards w/photographic backgrounds doing yoga. I'd like mine to stand out for it's line-drawn "cartoonish" nature, solid-color nature. The wording would be my basic contact info and a short description ... something like: "Experience the Magic of Mandala Making ... Next Class will be held: (open space for writing, no lines) The art is contained in this Facebook folder. Lots to choose from, with my favorites being the stronger outlined designs.

https://www.sketchnook.example/Brightloom/media_set?set=a.20262926615637197.2184852941.783542196&type=3
Updates

I just uploaded a few new drawings that might work better, since they are more round. I want to minimize the white space, for instance, avoid having the left & right corners empty. Another idea could be to use 1/4 mandalas in the corners. I'm ready to make a decision. I want it to look great, but as I gain drawing experience, I'll need to update my cards. Thanks! I'm not sure if this the place for this comment, but I'll also be needing a DVD label for my tutorials, and a front page design for a mandala coloring book.

Target Market(s)

Primarily women interested in metaphysical, psychic, meditation, reiki and a basic interest in art.

Font styles to use
Serif
Sans Serif

Requirements
Should not have
• Should not be on a dark card, really should be a plain white background, it seems, in order to stand out.

```html
<!DOCTYPE html>
<html lang="en">
<head>
<meta charset="UTF-8">
<title>Experience the Magic of Mandala Making – Postcard</title>
<link rel="stylesheet" href="https://fonts.googleapis.com/css2?family=Abril+Fatface&family=Oswald:wght@700&display=swap">
<style>
  :root {
    --paper: #ffffff;
    --ink: #111111;
    --rose: #f0457a;
    --magenta: #c8288a;
    --blush: #f49ae8;
    --lime: #a6ef3a;
    --aqua: #4de8d6;
    --note-fill: #d8d8d8;
    --note-edge: #a8a8a8;
    --mandala-core: #f4a07a;
    --mandala-mid: #3fc9c4;
    --mandala-outer: #e8327f;
  }
  html, body {
    margin: 0;
    padding: 0;
    width: 1200px;
    height: 1000px;
    overflow: hidden;
    background: var(--paper);
  }
  .postcard {
    position: relative;
    width: 1200px;
    height: 1000px;
    background: var(--paper);
    overflow: hidden;
  }
  .mandala-art {
    position: absolute;
    left: 0;
    top: 0;
    width: 1200px;
    height: 1000px;
  }
  .headline {
    position: absolute;
    left: 750px;
    top: 357px;
    width: 357px;
    height: 430px;
    margin: 0;
    transform: rotate(-90deg);
    transform-origin: 0 0;
    font-family: "Abril Fatface", serif;
    font-weight: 400;
    font-size: 66px;
    line-height: 86px;
    letter-spacing: -1px;
    white-space: nowrap;
  }
  .headline span {
    display: block;
    text-shadow: 3px 3px 0 var(--ink);
  }
  .headline .line-experience { color: var(--rose); }
  .headline .line-magic { color: var(--magenta); }
  .headline .line-of { color: var(--blush); text-align: center; }
  .headline .line-mandala { color: var(--lime); }
  .headline .line-making { color: var(--aqua); font-size: 80px; line-height: 90px; }
  .next-class {
    position: absolute;
    left: 1066px;
    top: 691px;
    width: 290px;
    margin: 0;
    transform: rotate(-90deg);
    transform-origin: 0 0;
    font-family: "Oswald", sans-serif;
    font-weight: 700;
    font-size: 21px;
    line-height: 24px;
    color: var(--ink);
    white-space: nowrap;
  }
  .date-box {
    position: absolute;
    left: 1098px;
    top: 373px;
    width: 62px;
    height: 324px;
    background: var(--note-fill);
    border: 1px solid var(--note-edge);
    border-radius: 10px;
    box-sizing: border-box;
  }
</style>
</head>
<body>
  <main class="postcard">
    <svg class="mandala-art" viewBox="0 0 1200 1000" role="img" aria-label="Hand-coloured mandala drawing with petals, spikes and beaded rim in pink, lime, turquoise and peach, shown as a partial circle">
      <defs>
        <radialGradient id="mandala-tones" cx="404" cy="574" r="363" gradientUnits="userSpaceOnUse">
          <stop offset="0" stop-color="var(--mandala-core)"/>
          <stop offset="0.35" stop-color="var(--mandala-mid)"/>
          <stop offset="0.7" stop-color="#b8e84a"/>
          <stop offset="1" stop-color="var(--mandala-outer)"/>
        </radialGradient>
        <clipPath id="mandala-crop">
          <rect x="231" y="205" width="560" height="530"/>
        </clipPath>
        <filter id="mandala-shadow" x="-10%" y="-10%" width="120%" height="120%">
          <feDropShadow dx="6" dy="8" stdDeviation="7" flood-color="#000" flood-opacity="0.35"/>
        </filter>
      </defs>
      <g clip-path="url(#mandala-crop)">
        <circle cx="404" cy="574" r="363" fill="url(#mandala-tones)" filter="url(#mandala-shadow)"/>
      </g>
    </svg>

    <h1 class="headline">
      <span class="line-experience">Experience</span>
      <span class="line-magic">the Magic</span>
      <span class="line-of">of</span>
      <span class="line-mandala">Mandala</span>
      <span class="line-making">Making</span>
    </h1>

    <p class="next-class">Next Class will be held</p>
    <div class="date-box"></div>
  </main>
</body>
</html>
```